Business Card Design Project

Looking for a logo and business card for a Real State Business i will be opening. The name is not choosen yet , but will probably be RTV IMOVEIS.
I was thinking black and silver colors, but am open to nice ideas.
I did add a business card that i liked a lot, am looking for something like that, with logo in black or silver in a black card. The logo i was thinking in the letters RTV as i uploaded or something or little and cute buildings or a house...just ideas, can be any nice logo.
Updates

You guys can add other colors if you want, I like colors very "BRIGHT" and "open", like red, pink, strong colors. almost glow in the dark colors. lol

Designers,

I've increased more 88 dollars in the budget for 1st place cause I will want envelope designs... small and big sizes.

So 1st place is now U$248,00. 

No need to send the envelope designs right now... only the business cards designs.

Thank you.

Industry/Entity Type

Business

Requirements
Must have
• Renata Tavares Vilela

www.RTVimoveis-exemplo.com.br

+554188316402

renata@rtvimoveis-exemplo.com.br

```html
<!DOCTYPE html>
<html lang="pt-BR">
<head>
<meta charset="utf-8">
<title>RTV Imóveis – Cartão de visita</title>
<link rel="stylesheet" href="https://fonts.googleapis.com/css2?family=Aldrich&display=swap">
<style>
  :root {
    --stage-light: #8cc400;
    --stage-mid: #6fa800;
    --stage-dark: #3f6e00;
    --card-black: #1e1b1b;
    --logo-silver: #a3a3a3;
    --accent-yellow: #fff200;
  }
  * { margin: 0; padding: 0; box-sizing: border-box; }
  html, body { width: 1200px; height: 848px; overflow: hidden; }
  body {
    position: relative;
    font-family: "Aldrich", sans-serif;
    background: var(--stage-mid);
  }
  .stage-backdrop {
    position: absolute; inset: 0;
    background: radial-gradient(ellipse at 55% 40%, var(--stage-light) 0%, var(--stage-mid) 50%, var(--stage-dark) 100%);
  }
  .card {
    position: absolute;
    top: 312px;
    width: 363px;
    height: 222px;
    overflow: hidden;
    background: var(--card-black);
  }
  .card--front { left: 209px; }
  .card--back { left: 628px; }

  .front-logo {
    position: absolute;
    left: 0; right: 0; top: 44px;
    text-align: center;
    color: var(--logo-silver);
  }
  .front-logo__name {
    display: block;
    font-size: 92px;
    line-height: 1;
    letter-spacing: -2px;
  }
  .front-logo__sub {
    display: block;
    margin-top: 10px;
    font-size: 26px;
    line-height: 1;
    letter-spacing: 9px;
    padding-left: 9px;
  }

  .accent-band {
    position: absolute;
    top: 0; right: 0;
    width: 22px; height: 100%;
    background: var(--accent-yellow);
  }
  .accent-rule {
    position: absolute;
    left: 28px; top: 92px;
    width: 150px; height: 3px;
    background: var(--accent-yellow);
  }
  .back-logo {
    position: absolute;
    left: 28px; top: 24px;
    font-size: 58px;
    line-height: 1;
    letter-spacing: -1px;
    color: var(--logo-silver);
  }
  .holder-name {
    position: absolute;
    left: 28px; top: 112px;
    font-size: 19px;
    line-height: 1.2;
    color: var(--accent-yellow);
    white-space: nowrap;
  }
  .contact-list {
    position: absolute;
    right: 38px; top: 170px;
    list-style: none;
    text-align: right;
    font-size: 10.5px;
    line-height: 15.5px;
    color: var(--accent-yellow);
    white-space: nowrap;
  }
</style>
</head>
<body>
  <div class="stage-backdrop" role="img" aria-label="Fundo verde com curvas abstratas suaves"></div>

  <section class="card card--front" aria-label="Frente do cartão">
    <div class="front-logo">
      <span class="front-logo__name">RTV</span>
      <span class="front-logo__sub">imoveis</span>
    </div>
  </section>

  <section class="card card--back" aria-label="Verso do cartão">
    <div class="accent-band" aria-hidden="true"></div>
    <div class="back-logo">RTV</div>
    <div class="accent-rule" aria-hidden="true"></div>
    <p class="holder-name">Renata Tavares Vilela</p>
    <ul class="contact-list">
      <li>renata@rtvimoveis-exemplo.com.br</li>
      <li>www.RTVimoveis-exemplo.com.br</li>
      <li>+554 188 316 402</li>
    </ul>
  </section>
</body>
</html>
```